Copper Lantern LLC Business Card

We need a business card design for a newco in Texas. We are a team of professionals who join start ups as founders and help launch their businesses, which are primarily related to food and beverage and the service side of the industry. We love local and craft and are partners in businesses in the local meat, BBQ and Burger, fine dining, and beverage alcohol businesses. Our specialty is finance and the business side of start ups, including assisting with capital raises as principals, not brokers. We do not currently have any logos or graphics for this entity. Our values include helping people succeed, rooting for the underdog, healthy food, the environment and being good citizens.

Target Market(s)

Everybody but also Angel Investors, CPAs, Bankers, Entrepreneurs

Industry/Entity Type

Business

Contact Information for Business Card

Fields for Business Name, Title, Email Address, Phone Number. Place to add mailing address and web domain later.

Font styles to use
Sans Serif

Colors

Designer to choose colors to be used in the design.

Requirements
Should not have
• Pictures of booze bottles or drinks thought there could be a social scene that does not strictly focus on those. No cows, cowboy hats or ranches. We are not a Wall Street type entity so no huge office buildings or skylines.

```html
<!DOCTYPE html>
<html lang="en">
<head>
<meta charset="utf-8">
<title>Business Card</title>
<link rel="stylesheet" href="https://fonts.googleapis.com/css2?family=Ubuntu:wght@700&family=Open+Sans:wght@300;400;600&display=swap">
<style>
  :root {
    --card-red: #c70a1a;
    --card-red-deep: #c0000f;
    --card-charcoal: #363636;
    --card-white: #ffffff;
    --backdrop-light: #e2e2e2;
    --backdrop-dark: #9b9b9b;
  }
  * { box-sizing: border-box; margin: 0; padding: 0; }
  html, body {
    width: 1200px;
    height: 877px;
    overflow: hidden;
  }
  body {
    background: radial-gradient(ellipse at 35% 70%, var(--backdrop-light) 0%, var(--backdrop-dark) 75%);
    display: flex;
    align-items: center;
    justify-content: center;
    font-family: "Open Sans", sans-serif;
  }
  .business-card {
    position: relative;
    width: 860px;
    height: 500px;
    background: var(--card-charcoal);
    color: var(--card-white);
    overflow: hidden;
    box-shadow: 0 18px 40px rgba(0,0,0,0.25);
  }
  .brand-panel {
    position: absolute;
    left: 0; top: 0;
    width: 100%;
    height: 268px;
    background: var(--card-red);
  }
  .business-name {
    position: absolute;
    left: 220px;
    top: 140px;
    font-family: "Ubuntu", sans-serif;
    font-weight: 700;
    font-size: 50px;
    letter-spacing: 0.5px;
    line-height: 1;
    padding-bottom: 8px;
    border-bottom: 2px solid var(--card-white);
  }
  .divider-line {
    position: absolute;
    height: 3px;
    background: var(--card-white);
  }
  .divider-top { left: 0; top: 288px; width: 100%; }
  .divider-bottom { left: 0; top: 462px; width: 100%; }
  .divider-vertical {
    position: absolute;
    left: 390px;
    top: 291px;
    width: 3px;
    height: 171px;
    background: var(--card-white);
  }
  .person-panel {
    position: absolute;
    left: 0;
    top: 291px;
    width: 390px;
    height: 171px;
    background: var(--card-red-deep);
  }
  .person-name {
    position: absolute;
    right: 40px;
    top: 50px;
    font-weight: 600;
    font-size: 40px;
    line-height: 1;
    text-align: right;
  }
  .person-title {
    position: absolute;
    right: 40px;
    top: 96px;
    font-weight: 300;
    font-size: 24px;
    line-height: 1;
    text-align: right;
  }
  .contact-panel {
    position: absolute;
    left: 393px;
    top: 291px;
    width: 467px;
    height: 171px;
    padding: 14px 0 0 44px;
  }
  .contact-list {
    list-style: none;
    font-size: 24px;
    line-height: 28px;
  }
  .contact-item {
    display: flex;
    align-items: center;
    height: 28px;
  }
  .contact-icon {
    width: 22px;
    height: 22px;
    margin-right: 22px;
    flex: none;
    display: block;
  }
  .contact-item.no-icon { padding-left: 44px; }
</style>
</head>
<body>
  <article class="business-card">
    <div class="brand-panel">
      <h1 class="business-name">Business name</h1>
    </div>

    <div class="divider-line divider-top"></div>

    <section class="person-panel">
      <p class="person-name">John Smith</p>
      <p class="person-title">general manager</p>
    </section>

    <div class="divider-vertical"></div>

    <section class="contact-panel">
      <ul class="contact-list">
        <li class="contact-item">
          <svg class="contact-icon" viewBox="0 0 24 24" aria-label="phone">
            <path fill="#fff" d="M6.6 3.5l2.6 3.4-1.6 1.9c.9 2 2.6 3.9 4.9 5.2l1.8-1.6 3.5 2.5-1.6 3.1c-5.8-.6-11-5.9-11.4-11.9z"/>
          </svg>
          <span>+1 555 01 02 33</span>
        </li>
        <li class="contact-item">
          <svg class="contact-icon" viewBox="0 0 24 24" aria-label="email">
            <text x="12" y="18" text-anchor="middle" fill="#fff" font-family="Open Sans, sans-serif" font-size="20" font-weight="600">@</text>
          </svg>
          <span>johnsmith@example.com</span>
        </li>
        <li class="contact-item">
          <svg class="contact-icon" viewBox="0 0 24 24" aria-label="website">
            <g fill="none" stroke="#fff" stroke-width="1.6">
              <circle cx="12" cy="12" r="9"/>
              <ellipse cx="12" cy="12" rx="4" ry="9"/>
              <line x1="3" y1="12" x2="21" y2="12"/>
              <line x1="4.5" y1="7.5" x2="19.5" y2="7.5"/>
              <line x1="4.5" y1="16.5" x2="19.5" y2="16.5"/>
            </g>
          </svg>
          <span>www.example.com</span>
        </li>
        <li class="contact-item">
          <svg class="contact-icon" viewBox="0 0 24 24" aria-label="mail">
            <rect x="2.5" y="6" width="19" height="13" fill="#fff"/>
            <path d="M2.5 6l9.5 7.5L21.5 6M2.5 19l7-6M21.5 19l-7-6" fill="none" stroke="#363636" stroke-width="1.4"/>
          </svg>
          <span>po box 742, Texas</span>
        </li>
        <li class="contact-item no-icon">
          <span>TX 7421</span>
        </li>
      </ul>
    </section>

    <div class="divider-line divider-bottom"></div>
  </article>
</body>
</html>
```